Car Wash MENU BOARD SIGN - GLEAM YARD CAR WASH

We are after a fresh new design for our new car wash packages. The new menu board will be a sign that is placed next to the payment system where they purchase their wash.

Our business name is called Gleam Yard. Our colours are Black background with Yellow Font. We also use blue in our logo.

Our package options are Ultimate, Deluxe and Standard. The pricing is:
$17 Ultimate
$13 Deluxe
$9 Standard

We also have a special offer which is called Loyal Six. The customer buys 5 and gets 1 free. The cost p/wash works out to be:
Ultimate $14.16 p/wash
Deluxe $10.83 p/wash
Standard $7.50 p/wash

Our Wash Packages are:
Ultimate Deluxe Standard
Pre-Wash Y Y Y
Soft Wash Y Y Y
Wheel Wash Y Y
Dry Y Y

Heron Polish Tide Y Y Y
Heron Polish Moss Y Y
Heron Polish Rapid Sheen Y

Car Wash customers

Club

• Must have logos of:
• Heron Polish Tide
• Heron Polish Moss
• Heron Polish Rapid Sheen
• Clearly show 3 different car wash packages
• Have the order of car washes options displayed in the exact order provided

```html
<!DOCTYPE html>
<html lang="en">
<head>
<meta charset="utf-8">
<title>Gleam Yard Car Wash – Wash Packages</title>
<link rel="stylesheet" href="https://fonts.googleapis.com/css2?family=Oswald:wght@600&family=Open+Sans:wght@600;700&family=Roboto:wght@900&display=swap">
<style>
  :root {
    --board-black: #000000;
    --brand-yellow: #f2da12;
    --brand-blue: #1b9ad1;
    --band-dark: #505152;
    --band-light: #7a7b7d;
    --pass-blue-top: #1a8fd8;
    --pass-blue-bottom: #0a3f93;
    --hot-orange: #f0751e;
    --hot-orange-light: #f9a23a;
    --white: #ffffff;
  }
  * { margin: 0; padding: 0; box-sizing: border-box; }
  html, body { width: 923px; height: 1200px; overflow: hidden; background: var(--board-black); }
  .menu-board { position: relative; width: 923px; height: 1200px; background: var(--board-black); overflow: hidden; }

  .board-heading {
    position: absolute; right: 20px; top: 18px;
    font-family: "Oswald", sans-serif; font-weight: 600; font-size: 72px; line-height: 1;
    color: var(--brand-yellow); letter-spacing: -1px; transform: scaleX(0.86); transform-origin: right top;
  }

  .package-band {
    position: absolute; left: 119px; right: 0;
    background: linear-gradient(90deg, var(--band-dark), var(--band-light));
  }
  .band-ultimate { top: 111px; height: 285px; }
  .band-deluxe { top: 419px; height: 287px; }
  .band-standard { top: 728px; height: 286px; }

  .package-number {
    position: absolute; font-family: "Roboto", sans-serif; font-weight: 900;
    font-size: 430px; line-height: 1; color: var(--brand-blue); z-index: 2;
  }
  .number-one { left: 20px; top: 36px; font-style: italic; }
  .number-two { left: -14px; top: 350px; }
  .number-three { left: -10px; top: 660px; }

  .package-title {
    position: absolute; z-index: 3;
    font-family: "Oswald", sans-serif; font-weight: 600; font-size: 76px; line-height: 1;
    color: var(--brand-yellow); transform: scaleX(0.88); transform-origin: left top; white-space: nowrap;
  }

  .feature-list { position: absolute; list-style: none; z-index: 3; }
  .feature-list li {
    display: flex; align-items: center; gap: 10px; height: 36px;
    font-family: "Open Sans", sans-serif; font-weight: 600; font-size: 25px; color: var(--brand-yellow);
  }
  .feature-list svg { width: 25px; height: 25px; flex: none; }

  .product-badge { position: absolute; z-index: 3; border-radius: 10px; }
  .badge-tide { background: linear-gradient(180deg, #f7b02c, #e0501a); }
  .badge-moss { background: linear-gradient(180deg, #3a9be0, #0e3d8a); border-radius: 50% / 40%; }
  .badge-rapid { background: linear-gradient(180deg, #f0a02a, #b8321a); transform: rotate(-14deg); border-radius: 8px; }

  .pass-card {
    position: absolute; left: 735px; width: 163px; z-index: 3;
  }
  .pass-panel {
    position: absolute; left: 0; right: 0; bottom: 0; top: 36px; border-radius: 8px;
    background: linear-gradient(180deg, var(--pass-blue-top), var(--pass-blue-bottom));
    padding: 56px 12px 0 0; text-align: right; color: var(--white);
    font-family: "Open Sans", sans-serif;
  }
  .pass-flame {
    position: absolute; left: 8px; top: 0; width: 150px; height: 82px; z-index: 1;
    border-radius: 50px 60px 70px 40px;
    background: linear-gradient(90deg, var(--hot-orange) 0%, var(--hot-orange-light) 70%, rgba(249,162,58,0) 100%);
  }
  .pass-hot {
    position: absolute; left: 10px; top: 8px; width: 76px; height: 76px; z-index: 2; border-radius: 50%;
    background: var(--hot-orange); color: var(--board-black);
    font-family: "Oswald", sans-serif; font-weight: 600; font-size: 22px; line-height: 0.95;
    display: flex; flex-direction: column; align-items: center; justify-content: center; text-align: center;
  }
  .pass-name { font-weight: 700; font-size: 36px; line-height: 1.0; }
  .pass-unit { font-weight: 600; font-size: 13px; margin-top: 6px; font-style: italic; }
  .pass-price { font-weight: 700; font-size: 32px; line-height: 1.05; }

  .brand-signoff {
    position: absolute; right: 14px; top: 1052px; display: flex; align-items: center; gap: 22px;
    font-family: "Oswald", sans-serif; font-weight: 600; font-size: 118px; line-height: 1;
    color: var(--brand-yellow);
  }
  .brand-dot { width: 64px; height: 64px; border-radius: 50%; background: var(--brand-blue); }
</style>
</head>
<body>
<main class="menu-board">
  <h1 class="board-heading">WASH PACKAGES</h1>

  <div class="package-band band-ultimate"></div>
  <div class="package-band band-deluxe"></div>
  <div class="package-band band-standard"></div>

  <span class="package-number number-one">1</span>
  <span class="package-number number-two">2</span>
  <span class="package-number number-three">3</span>

  <!-- Ultimate -->
  <h2 class="package-title" style="left:207px; top:140px;">ULTIMATE $17</h2>
  <ul class="feature-list" style="left:207px; top:225px;">
    <li><svg viewBox="0 0 24 24"><rect x="2" y="4" width="17" height="17" rx="3" fill="none" stroke="#1b9ad1" stroke-width="2.5"/><path d="M6 12l4 4 11-12" fill="none" stroke="#1b9ad1" stroke-width="3"/></svg>Pre-Wash</li>
    <li><svg viewBox="0 0 24 24"><rect x="2" y="4" width="17" height="17" rx="3" fill="none" stroke="#1b9ad1" stroke-width="2.5"/><path d="M6 12l4 4 11-12" fill="none" stroke="#1b9ad1" stroke-width="3"/></svg>Soft Wash</li>
    <li><svg viewBox="0 0 24 24"><rect x="2" y="4" width="17" height="17" rx="3" fill="none" stroke="#1b9ad1" stroke-width="2.5"/><path d="M6 12l4 4 11-12" fill="none" stroke="#1b9ad1" stroke-width="3"/></svg>Wheel Wash</li>
    <li><svg viewBox="0 0 24 24"><rect x="2" y="4" width="17" height="17" rx="3" fill="none" stroke="#1b9ad1" stroke-width="2.5"/><path d="M6 12l4 4 11-12" fill="none" stroke="#1b9ad1" stroke-width="3"/></svg>Dry</li>
  </ul>
  <div class="product-badge badge-tide" role="img" aria-label="Heron Polish Tide product badge" style="left:497px; top:230px; width:72px; height:66px;"></div>
  <div class="product-badge badge-moss" role="img" aria-label="Heron Polish Moss product badge" style="left:488px; top:314px; width:92px; height:58px;"></div>
  <div class="product-badge badge-rapid" role="img" aria-label="Heron Polish Rapid Sheen product badge" style="left:596px; top:272px; width:112px; height:52px;"></div>
  <div class="pass-card" style="top:146px; height:225px;">
    <div class="pass-flame" role="img" aria-label="Orange flame swoosh"></div>
    <div class="pass-hot">HOT<br>PRICE</div>
    <div class="pass-panel">
      <div class="pass-name">Loyal<br>Six</div>
      <div class="pass-unit">per wash</div>
      <div class="pass-price">$14.16</div>
    </div>
  </div>

  <!-- Deluxe -->
  <h2 class="package-title" style="left:246px; top:452px;">DELUXE $13</h2>
  <ul class="feature-list" style="left:237px; top:539px;">
    <li><svg viewBox="0 0 24 24"><rect x="2" y="4" width="17" height="17" rx="3" fill="none" stroke="#1b9ad1" stroke-width="2.5"/><path d="M6 12l4 4 11-12" fill="none" stroke="#1b9ad1" stroke-width="3"/></svg>Pre-Wash</li>
    <li><svg viewBox="0 0 24 24"><rect x="2" y="4" width="17" height="17" rx="3" fill="none" stroke="#1b9ad1" stroke-width="2.5"/><path d="M6 12l4 4 11-12" fill="none" stroke="#1b9ad1" stroke-width="3"/></svg>Soft Wash</li>
    <li><svg viewBox="0 0 24 24"><rect x="2" y="4" width="17" height="17" rx="3" fill="none" stroke="#1b9ad1" stroke-width="2.5"/><path d="M6 12l4 4 11-12" fill="none" stroke="#1b9ad1" stroke-width="3"/></svg>Wheel Wash</li>
    <li><svg viewBox="0 0 24 24"><rect x="2" y="4" width="17" height="17" rx="3" fill="none" stroke="#1b9ad1" stroke-width="2.5"/><path d="M6 12l4 4 11-12" fill="none" stroke="#1b9ad1" stroke-width="3"/></svg>Dry</li>
  </ul>
  <div class="product-badge badge-tide" role="img" aria-label="Heron Polish Tide product badge" style="left:500px; top:545px; width:72px; height:66px;"></div>
  <div class="product-badge badge-moss" role="img" aria-label="Heron Polish Moss product badge" style="left:492px; top:628px; width:90px; height:60px;"></div>
  <div class="pass-card" style="top:456px; height:225px;">
    <div class="pass-flame" role="img" aria-label="Orange flame swoosh"></div>
    <div class="pass-hot">HOT<br>PRICE</div>
    <div class="pass-panel">
      <div class="pass-name">Loyal<br>Six</div>
      <div class="pass-unit">per wash</div>
      <div class="pass-price">$10.83</div>
    </div>
  </div>

  <!-- Standard -->
  <h2 class="package-title" style="left:232px; top:765px;">STANDARD $9</h2>
  <ul class="feature-list" style="left:232px; top:869px;">
    <li><svg viewBox="0 0 24 24"><rect x="2" y="4" width="17" height="17" rx="3" fill="none" stroke="#1b9ad1" stroke-width="2.5"/><path d="M6 12l4 4 11-12" fill="none" stroke="#1b9ad1" stroke-width="3"/></svg>Pre-Wash</li>
    <li><svg viewBox="0 0 24 24"><rect x="2" y="4" width="17" height="17" rx="3" fill="none" stroke="#1b9ad1" stroke-width="2.5"/><path d="M6 12l4 4 11-12" fill="none" stroke="#1b9ad1" stroke-width="3"/></svg>Soft Wash</li>
  </ul>
  <div class="product-badge badge-tide" role="img" aria-label="Heron Polish Tide product badge" style="left:494px; top:876px; width:72px; height:68px;"></div>
  <div class="pass-card" style="top:769px; height:223px;">
    <div class="pass-flame" role="img" aria-label="Orange flame swoosh"></div>
    <div class="pass-hot">HOT<br>PRICE</div>
    <div class="pass-panel">
      <div class="pass-name">Loyal<br>Six</div>
      <div class="pass-unit">per wash</div>
      <div class="pass-price">$7.50</div>
    </div>
  </div>

  <footer class="brand-signoff">
    <span class="brand-dot"></span>
    <span class="brand-name">GLEAM YARD</span>
  </footer>
</main>
</body>
</html>
```